Fence Flyer to Attract More Sales During Winter

We need a new flyer made that we can distribute to residential mailboxes. The flyer is to promote our Frostline Picket Days. We like simply designs, and we would like the flyer to showcase a lot of our fence photos. More of our photos are online at our website at www.getbramblerail.com - our new address needs to also be featured on the flyer - 436 Quillen rd, Monroe, NC 28117. I do want the words "FROSTLINE PICKET DAYS" to be dominate on the flyer with the description "Wood fences starting at $12/FT!" Please look through our Facebook page and our website to gather more photos or information. We are flexible on colors, nothing to fancy - simple flyer design please.

Target Market(s)

Residential homeowners that need a new fence to enclose their yard for safety, security or decorative

Industry/Entity Type

Residential Construction

Font styles to use
Sans Serif

Colors

Designer to choose colors to be used in the design.

Requirements
Must have
• Frostline Picket Days
• Contact information for the business
• "Come visit our outdoor showroom, open 24/7!"
Nice to have
• Photos of our fences - you can find more on our website at www.GetBrambleRail.com or Facebook.com/MeadowlarkRailGPV
Should not have
• Flashy designs

```html
<!DOCTYPE html>
<html lang="en">
<head>
<meta charset="utf-8">
<title>Frostline Picket Days Flyer</title>
<link href="https://fonts.googleapis.com/css2?family=Montserrat:wght@500;700;800&display=swap" rel="stylesheet">
<style>
  :root{
    --page-bg:#e9e6e1;
    --panel-brown:#5a4126;
    --accent-yellow:#f2e21a;
    --ink-white:#ffffff;
    --wood-light:#d7b98a;
    --grass:#5f8f3a;
    --dirt:#a0633a;
    --sky:#9fb4c8;
  }
  *{box-sizing:border-box;margin:0;padding:0}
  html,body{width:1200px;height:800px;overflow:hidden;background:var(--page-bg)}
  body{font-family:"Montserrat",sans-serif;position:relative}
  .flyer{position:absolute;left:320px;top:30px;width:560px;height:740px;background:var(--panel-brown);box-shadow:0 6px 18px rgba(0,0,0,.25);overflow:hidden}
  .photo{position:absolute}
  .photo--wood{background:linear-gradient(160deg,var(--sky) 0%,var(--wood-light) 35%,#8a7a5a 70%,#4d5e33 100%)}
  .photo--picket{background:linear-gradient(100deg,#d89a4e 0%,#e7b772 50%,#6c9a3e 100%)}
  .photo--iron{background:linear-gradient(170deg,#7fa3c9 0%,#3e6a2c 35%,#2b2b2b 55%,var(--grass) 75%,var(--dirt) 100%)}
  .photo--yard{background:linear-gradient(170deg,#4f7d32 0%,#d8d2c0 45%,var(--grass) 100%)}
  .panel{position:absolute;left:160px;top:190px;width:250px;height:550px;background:var(--panel-brown);color:var(--ink-white);text-align:center}
  .title-box{margin:22px auto 0;width:214px;border:5px solid var(--ink-white);padding:26px 0 24px}
  .title-line{display:block;font-weight:800;font-size:28px;line-height:1.15;letter-spacing:.5px}
  .title-accent{display:block;font-weight:800;font-size:24px;color:var(--accent-yellow);margin-top:6px}
  .offer-small{font-size:10px;font-weight:700;margin-top:14px}
  .offer-lead{font-size:20px;font-weight:800;margin-top:2px}
  .offer-price{font-size:44px;font-weight:800;color:var(--accent-yellow);line-height:1.05}
  .visit-come{font-size:38px;font-weight:800;color:var(--accent-yellow);margin-top:18px;line-height:1}
  .visit-our{font-size:20px;font-weight:800;line-height:1.1}
  .visit-showroom{font-size:10px;font-weight:700;color:var(--accent-yellow)}
  .hours{font-size:18px;font-weight:700;margin-top:26px;display:flex;align-items:center;justify-content:center;gap:8px}
  .hours::before,.hours::after{content:"";width:22px;height:2px;background:var(--ink-white)}
  .contact{margin-top:16px;padding-left:18px;text-align:left}
  .contact-row{display:flex;align-items:center;gap:6px;font-weight:700}
  .contact-row svg{flex:none}
  .contact-email{font-size:10px}
  .contact-phone{font-size:27px;font-weight:800;line-height:1.15}
  .contact-address{font-size:9.5px}
</style>
</head>
<body>
<main class="flyer">
  <div class="photo photo--wood" style="left:0;top:0;width:160px;height:190px" role="img" aria-label="Photo of a new wood privacy fence along a yard"></div>
  <div class="photo photo--picket" style="left:160px;top:0;width:120px;height:190px" role="img" aria-label="Photo of fresh wooden pickets"></div>
  <div class="photo photo--iron" style="left:280px;top:0;width:130px;height:190px" role="img" aria-label="Photo of a black metal garden gate"></div>
  <div class="photo photo--yard" style="left:410px;top:0;width:150px;height:190px" role="img" aria-label="Photo of a black metal fence along a lawn"></div>

  <div class="photo photo--wood" style="left:0;top:190px;width:160px;height:180px" role="img" aria-label="Photo of a wood fence beside a house"></div>
  <div class="photo photo--yard" style="left:0;top:370px;width:160px;height:180px" role="img" aria-label="Photo of a wood fence among trees"></div>
  <div class="photo photo--wood" style="left:0;top:550px;width:160px;height:190px" role="img" aria-label="Photo of a picket fence on a sunny lawn"></div>

  <div class="photo photo--iron" style="left:410px;top:190px;width:150px;height:190px" role="img" aria-label="Photo of a black metal fence on a dirt yard"></div>
  <div class="photo photo--iron" style="left:410px;top:380px;width:150px;height:180px" role="img" aria-label="Photo of a black metal fence around a pool"></div>
  <div class="photo photo--yard" style="left:410px;top:560px;width:150px;height:180px" role="img" aria-label="Photo of a black metal fence in a garden"></div>

  <section class="panel">
    <div class="title-box">
      <span class="title-line">FROSTLINE</span>
      <span class="title-line">PICKET</span>
      <span class="title-accent">DAYS</span>
    </div>
    <p class="offer-small">WOOD FENCES</p>
    <p class="offer-lead">STARTING AT</p>
    <p class="offer-price">$12/FT!</p>
    <p class="visit-come">COME</p>
    <p class="visit-our">VISIT OUR</p>
    <p class="visit-showroom">OUTDOOR SHOWROOM</p>
    <p class="hours">OPEN 24/7</p>
    <div class="contact">
      <p class="contact-row contact-email">
        <svg width="11" height="8" viewBox="0 0 11 8"><rect width="11" height="8" rx="1" fill="#f2e21a"/><path d="M0 0l5.5 4.5L11 0" stroke="#5a4126" fill="none"/></svg>
        OFFICE@GETBRAMBLERAIL.COM</p>
      <p class="contact-row contact-phone">
        <svg width="11" height="11" viewBox="0 0 24 24"><path fill="#f2e21a" d="M6.6 10.8a15 15 0 0 0 6.6 6.6l2.2-2.2a1 1 0 0 1 1-.25 11.4 11.4 0 0 0 3.6.57 1 1 0 0 1 1 1V20a1 1 0 0 1-1 1A17 17 0 0 1 3 4a1 1 0 0 1 1-1h3.5a1 1 0 0 1 1 1 11.4 11.4 0 0 0 .57 3.6 1 1 0 0 1-.25 1z"/></svg>
        704-555-0163</p>
      <p class="contact-row contact-address">
        <svg width="9" height="12" viewBox="0 0 24 32"><path fill="#f2e21a" d="M12 0a12 12 0 0 0-12 12c0 9 12 20 12 20s12-11 12-20A12 12 0 0 0 12 0zm0 17a5 5 0 1 1 0-10 5 5 0 0 1 0 10z"/></svg>
        436 QUILLEN RD, MONROE, NC 28117</p>
    </div>
  </section>
</main>
</body>
</html>
```